Q-Town Hoopers Needs Post Card Announcing Basketball Try Outs

TEXT
Q-TOWN HOOPERS
...a Neighborly Works Alliance Inc. program
(approved IRS 501C3)

BRAND NEW YSF Member Organization
Invites All Ballers / Boys and Girls / 2nd - 11th Grades

Open Gym Tryouts Start June 2014

Register for tryouts and join our emailing list by contacting us at....qtownhoopers@mailbox.example

Phone Contact Marcus Pendleton.(555) 482-9073
or visit us at www.qtownhoopers.example

```html
<!DOCTYPE html>
<html lang="en">
<head>
<meta charset="utf-8">
<title>Q-Town Hoopers – Tryouts Postcard</title>
<link rel="stylesheet" href="https://fonts.googleapis.com/css2?family=Oswald:wght@300;400;600&display=swap">
<style>
  :root {
    --backdrop: #e4e4e2;
    --card: #f7f7f5;
    --card-right: #fbfbfa;
    --rust: #bf5532;
    --rust-light: #d47a58;
    --ink: #2b2b2b;
    --ink-soft: #555555;
    --photo-dark: #3c3c3c;
    --photo-mid: #6a6a6a;
  }
  * { box-sizing: border-box; margin: 0; padding: 0; }
  html, body { width: 1200px; height: 1200px; overflow: hidden; }
  body {
    background: var(--backdrop);
    font-family: "Oswald", "Arial Narrow", sans-serif;
    position: relative;
  }
  .postcard {
    position: absolute;
    left: 324px;
    width: 552px;
    height: 426px;
    background: var(--card);
  }
  .postcard--front { top: 110px; }
  .postcard--back { top: 668px; }

  /* Front */
  .hoop-photo {
    position: absolute;
    left: 14px; top: 14px; right: 14px; bottom: 14px;
    background: radial-gradient(ellipse at 40% 40%, var(--photo-mid) 0%, var(--photo-dark) 75%);
  }
  .brand-banner {
    position: absolute;
    left: 344px; top: 0;
    width: 192px; height: 212px;
    background: rgba(191, 85, 50, 0.92);
    clip-path: polygon(0 0, 100% 0, 100% 82%, 0 100%);
    color: #fff;
    text-align: center;
  }
  .brand-banner__strip {
    height: 14px;
    background: var(--rust-light);
  }
  .brand-banner__mark {
    width: 76px; height: 76px;
    margin: 22px auto 0;
    border: 3px solid #fff;
    border-radius: 50%;
  }
  .brand-banner__name {
    margin-top: 18px;
    font-weight: 400;
    font-size: 24px;
    letter-spacing: 0.5px;
    line-height: 1;
  }

  /* Back */
  .postcard--back::after {
    content: "";
    position: absolute;
    left: 278px; top: 0; right: 0; bottom: 0;
    background: var(--card-right);
  }
  .back-brand {
    position: absolute;
    left: 28px; top: 40px;
    display: flex; align-items: center; gap: 12px;
  }
  .back-brand__mark {
    width: 48px; height: 48px;
    border: 2px solid var(--rust);
    border-radius: 50%;
  }
  .back-brand__name {
    font-weight: 400;
    font-size: 29px;
    color: var(--ink);
    line-height: 1;
  }
  .invite-panel {
    position: absolute;
    left: 0; top: 126px;
    width: 278px; height: 198px;
    background: var(--rust);
    color: #fbe7dd;
    padding: 22px 26px 0 26px;
    font-weight: 300;
    font-size: 12px;
    line-height: 14.5px;
    z-index: 1;
  }
  .invite-panel p + p { margin-top: 14px; }
  .invite-panel .tryout-date {
    font-weight: 600;
    font-size: 13.5px;
    letter-spacing: 0.5px;
    color: #fff;
  }
  .contact-list {
    position: absolute;
    left: 26px; top: 328px;
    font-size: 11px;
    font-weight: 300;
    color: var(--ink-soft);
    list-style: none;
    line-height: 18.5px;
  }
  .contact-list strong { font-weight: 600; color: var(--ink); }
  .address-side {
    position: absolute;
    left: 0; top: 0;
    z-index: 1;
  }
</style>
</head>
<body>

  <section class="postcard postcard--front" aria-label="Postcard front">
    <div class="hoop-photo" role="img" aria-label="Close-up photo of a basketball hoop and white net against a blurred grey gym"></div>
    <div class="brand-banner">
      <div class="brand-banner__strip"></div>
      <div class="brand-banner__mark"></div>
      <div class="brand-banner__name">Q-TOWN HOOPERS</div>
    </div>
  </section>

  <section class="postcard postcard--back" aria-label="Postcard back">
    <div class="back-brand" style="z-index:1">
      <span class="back-brand__mark"></span>
      <span class="back-brand__name">Q-TOWN HOOPERS</span>
    </div>

    <div class="invite-panel">
      <p>...a Neighborly Works Alliance Inc. program<br>(approved IRS 501C3)</p>
      <p>BRAND NEW YSF Member Organization<br>Invites All Ballers / Boys and Girls / 2nd - 11th<br>Grades</p>
      <p class="tryout-date">OPEN GYM TRYOUTS START JUNE 2014</p>
      <p>Register for tryouts and join our emailing list by<br>contacting us</p>
    </div>

    <ul class="contact-list" style="z-index:1">
      <li><strong>Contact</strong> | Marcus Pendleton</li>
      <li><strong>PHN.</strong> (555) 482-9073</li>
      <li><strong>WEB.</strong> QTOWNHOOPERS@MAILBOX.EXAMPLE</li>
      <li><strong>WEB.</strong> QTOWNHOOPERS.EXAMPLE</li>
    </ul>

    <svg class="address-side" width="552" height="426" viewBox="0 0 552 426" aria-hidden="true">
      <rect x="438.5" y="51.5" width="89" height="95" fill="none" stroke="#bf5532" stroke-width="1.5"/>
      <g stroke="#d47a58" stroke-width="1">
        <line x1="296" y1="193.5" x2="528" y2="193.5"/>
        <line x1="296" y1="226.5" x2="528" y2="226.5"/>
        <line x1="296" y1="258.5" x2="528" y2="258.5"/>
        <line x1="296" y1="290.5" x2="528" y2="290.5"/>
        <line x1="296" y1="323.5" x2="528" y2="323.5"/>
      </g>
    </svg>
  </section>

</body>
</html>
```